Business Image

I have recently had a new company logo made up and require some new business cards to go with it.

Target Market(s)

Developers & high worth clients.

Industry/Entity Type

Business

Contact Information for Business Card

The business is in the construction/management industry. It needs to be classy but have a industrial feel. I would like the business card to be a elegant presentation in itself.

Requirements
Must have
• Current logo & company name. Colouring needs to be the same as the current design also.
Nice to have
• A few different designs & presentations of single and double sided business cards.

```html
<!DOCTYPE html>
<html lang="en">
<head>
<meta charset="utf-8">
<title>Northhall Build Group – Business Card</title>
<link rel="stylesheet" href="https://fonts.googleapis.com/css2?family=Tinos&family=Roboto:wght@400&display=swap">
<style>
  :root {
    --backdrop: #2b2724;
    --card: #1b1b1d;
    --card-edge: #232325;
    --accent-blue: #3aa3e8;
    --mark-grey: #3c3c3f;
    --text-light: #f1f1f1;
    --text-muted: #bdbdbd;
  }
  * { margin: 0; padding: 0; box-sizing: border-box; }
  html, body { width: 1200px; height: 715px; overflow: hidden; }
  body {
    background: var(--backdrop);
    position: relative;
    font-family: "Roboto", Arial, sans-serif;
  }
  .card {
    position: absolute;
    top: 209px;
    width: 520px;
    height: 297px;
    background: linear-gradient(135deg, var(--card-edge) 0%, var(--card) 60%);
    border-radius: 4px;
    box-shadow: 0 12px 30px rgba(0,0,0,0.45);
  }
  .card--front { left: 50px; }
  .card--back { left: 630px; }

  .front-name {
    position: absolute;
    inset: 0;
    display: flex;
    align-items: center;
    justify-content: center;
    gap: 14px;
  }
  .front-name__square {
    width: 18px; height: 18px;
    background: var(--mark-grey);
  }
  .front-name__text {
    font-family: "Tinos", "Times New Roman", serif;
    font-size: 30px;
    color: var(--mark-grey);
    letter-spacing: 1px;
    text-transform: uppercase;
  }

  .company-name {
    position: absolute;
    left: 30px;
    top: 112px;
    width: 220px;
    font-family: "Tinos", "Times New Roman", serif;
    font-size: 25px;
    line-height: 1.1;
    color: var(--accent-blue);
    text-transform: uppercase;
  }

  .contact {
    position: absolute;
    left: 290px;
    top: 112px;
  }
  .contact__name {
    font-family: "Tinos", "Times New Roman", serif;
    font-size: 22px;
    color: var(--accent-blue);
  }
  .contact__role {
    font-size: 11px;
    color: var(--text-muted);
    margin-bottom: 12px;
  }
  .contact__row {
    display: flex;
    align-items: center;
    gap: 10px;
    font-size: 13px;
    color: var(--text-light);
    line-height: 21px;
    white-space: nowrap;
  }
  .contact__icon { width: 12px; height: 12px; fill: var(--text-light); flex: none; }
</style>
</head>
<body>
  <section class="card card--front" aria-label="Card front">
    <div class="front-name">
      <span class="front-name__square"></span>
      <span class="front-name__text">Northhall</span>
    </div>
  </section>

  <section class="card card--back" aria-label="Card back">
    <div class="company-name">Northhall Build Group</div>

    <div class="contact">
      <div class="contact__name">Daniel Reyes</div>
      <div class="contact__role">Director</div>
      <div class="contact__row">
        <svg class="contact__icon" viewBox="0 0 12 12"><path d="M2 1h2.5l1 3-1.5 1a6 6 0 0 0 3 3l1-1.5 3 1V10a1 1 0 0 1-1 1A9 9 0 0 1 1 2a1 1 0 0 1 1-1z"/></svg>
        <span>555-0142-7788</span>
      </div>
      <div class="contact__row">
        <svg class="contact__icon" viewBox="0 0 12 12"><path d="M0 2h12v8H0z M0 2l6 4 6-4" fill="none" stroke="#f1f1f1" stroke-width="1.2"/></svg>
        <span>daniel@northhallbuild.com</span>
      </div>
      <div class="contact__row">
        <svg class="contact__icon" viewBox="0 0 12 12"><g fill="none" stroke="#f1f1f1" stroke-width="1"><circle cx="6" cy="6" r="5"/><ellipse cx="6" cy="6" rx="2.2" ry="5"/><path d="M1 6h10"/></g></svg>
        <span>www.northhallbuild.com</span>
      </div>
    </div>
  </section>
</body>
</html>
```